Instagram Advert of Mobile App Launch event

I need an instagram post for a new mobile application for the launching campaign. The mobile application is for booking appointments in salons and with makeup artists (freelancers).

The target audience are the clients where we`ll ask them to tag their friends, download the app and create an account.

A draw will take a place after 1 week, and the winner and the tagged friend will get a Veloriane bracelet.

The post should contain the app logo (attached) and Veloriane logo.

Target Market(s)

Ladies in Kuwait only

Industry/Entity Type

Beauty Salon

Colors
ec1f27
ffc214
e667a6
e34197
a64599
f04a50

Requirements
Must have
• the app logo, Veloriane logo and to be modern style
Nice to have
• salon tools like makeup, hair brush, scissor,...
Should not have
• no human models

```html
<!DOCTYPE html>
<html lang="en">
<head>
<meta charset="utf-8">
<title>Lumira – App Launch Giveaway</title>
<link rel="stylesheet" href="https://fonts.googleapis.com/css2?family=Montserrat:wght@400;500;700&display=swap">
<style>
  :root {
    --red: #ec1f27;
    --yellow: #ffc214;
    --pink: #e667a6;
    --magenta: #e34197;
    --purple: #a64599;
    --coral: #f04a50;
    --plum: #8e2a6e;
    --grey: #8a8a90;
    --ink: #2a2a2e;
    --paper: #ffffff;
    --screen: #f6eef3;
  }
  * { box-sizing: border-box; margin: 0; padding: 0; }
  html, body { width: 1200px; height: 1200px; overflow: hidden; background: var(--paper); }
  body { font-family: "Montserrat", Arial, sans-serif; }

  .post { position: relative; width: 1200px; height: 1200px; overflow: hidden; background: var(--paper); }

  .splash {
    position: absolute; inset: 0;
    background:
      radial-gradient(ellipse 200px 240px at 560px 170px, rgba(255,194,20,.5), transparent 75%),
      radial-gradient(ellipse 260px 240px at 660px 420px, rgba(247,150,60,.42), transparent 75%),
      radial-gradient(ellipse 340px 300px at 720px 720px, rgba(240,74,80,.42), transparent 75%),
      radial-gradient(ellipse 380px 270px at 860px 1010px, rgba(227,65,151,.5), transparent 75%),
      radial-gradient(ellipse 220px 240px at 1120px 1090px, rgba(166,69,153,.7), transparent 75%);
  }
  .splash-drop { position: absolute; border-radius: 50%; background: var(--coral); opacity: .85; }

  .tools {
    position: absolute; left: 470px; top: -40px; width: 380px; height: 1240px;
    transform: rotate(16deg); transform-origin: top center;
    background:
      radial-gradient(ellipse 150px 200px at 50% 12%, rgba(230,200,40,.55), transparent 80%),
      radial-gradient(ellipse 150px 200px at 50% 36%, rgba(190,110,70,.4), transparent 80%),
      radial-gradient(ellipse 150px 220px at 50% 60%, rgba(150,60,80,.35), transparent 80%),
      radial-gradient(ellipse 150px 220px at 50% 84%, rgba(90,60,80,.3), transparent 80%);
  }

  .brand { position: absolute; right: 78px; top: 44px; display: flex; flex-direction: column; align-items: center; gap: 12px; }
  .brand-dot { width: 98px; height: 98px; border-radius: 50%; background: var(--magenta); }
  .brand-name { font-size: 48px; font-weight: 500; color: var(--grey); letter-spacing: 1px; }

  .phone {
    position: absolute; left: 110px; top: 165px; width: 410px; height: 660px;
    transform: rotate(8deg);
    background: #f2f2f4; border: 3px solid #d3d3d8; border-radius: 58px;
    box-shadow: 0 18px 40px rgba(0,0,0,.18);
  }
  .phone-speaker { position: absolute; left: 50%; top: 40px; width: 60px; height: 7px; margin-left: -30px; border-radius: 4px; background: #2b2b2f; }
  .phone-camera { position: absolute; left: 130px; top: 37px; width: 12px; height: 12px; border-radius: 50%; background: #2b2b2f; }
  .phone-home { position: absolute; left: 50%; bottom: 22px; width: 44px; height: 44px; margin-left: -22px; border-radius: 50%; border: 2px solid #bdbdc3; }
  .phone-screen {
    position: absolute; left: 20px; right: 20px; top: 80px; bottom: 84px;
    border: 2px solid #2b2b2f;
    background: linear-gradient(180deg, #fbf7fa 0%, var(--screen) 55%, #e9d3e0 100%);
    display: flex; flex-direction: column; align-items: center; text-align: center;
    padding-top: 46px;
  }
  .app-dot { width: 64px; height: 64px; border-radius: 50%; background: var(--magenta); }
  .app-name { margin-top: 8px; font-size: 34px; font-weight: 500; color: var(--grey); }
  .screen-kicker { margin-top: 40px; font-size: 19px; font-weight: 700; color: var(--magenta); }
  .screen-lead { margin-top: 6px; font-size: 19px; font-weight: 500; line-height: 1.2; color: #6c6c78; text-transform: uppercase; }
  .screen-actions { margin-top: auto; margin-bottom: 50px; width: 86%; display: flex; flex-direction: column; gap: 14px; }
  .btn { height: 40px; border-radius: 12px; font-size: 14px; display: flex; align-items: center; justify-content: center; }
  .btn-primary { background: var(--plum); color: var(--paper); }
  .btn-secondary { background: var(--paper); color: var(--ink); }

  .prize { position: absolute; left: 0; top: 860px; width: 380px; height: 340px; }
  .prize-art {
    position: absolute; inset: 0;
    background:
      radial-gradient(ellipse 190px 90px at 55% 32%, rgba(236,31,39,.85), transparent 80%),
      radial-gradient(ellipse 220px 220px at 30% 70%, rgba(225,225,230,.9), transparent 85%);
  }
  .prize-name { position: absolute; left: 190px; top: 88px; transform: rotate(8deg); font-size: 26px; font-weight: 500; color: var(--paper); }
</style>
</head>
<body>
<main class="post">
  <div class="splash" role="img" aria-label="Watercolour splash fading from yellow through orange and red to purple"></div>
  <span class="splash-drop" style="left:1005px;top:798px;width:16px;height:16px"></span>
  <span class="splash-drop" style="left:1048px;top:815px;width:9px;height:9px"></span>
  <span class="splash-drop" style="left:1092px;top:818px;width:12px;height:12px"></span>
  <span class="splash-drop" style="left:1150px;top:808px;width:20px;height:20px"></span>

  <div class="tools" role="img" aria-label="Beauty tools arranged diagonally: mascara wands, makeup brushes, lipstick, comb and scissors"></div>

  <header class="brand">
    <span class="brand-dot"></span>
    <span class="brand-name">Lumira</span>
  </header>

  <section class="phone">
    <span class="phone-camera"></span>
    <span class="phone-speaker"></span>
    <div class="phone-screen">
      <span class="app-dot"></span>
      <span class="app-name">Lumira</span>
      <p class="screen-kicker">FIND AND BOOK</p>
      <p class="screen-lead">Hair, Make Up<br>Beauty Salons and<br>Professionals</p>
      <div class="screen-actions">
        <span class="btn btn-primary">Create New Account</span>
        <span class="btn btn-secondary">Log In</span>
      </div>
    </div>
    <span class="phone-home"></span>
  </section>

  <aside class="prize">
    <div class="prize-art" role="img" aria-label="Gift box tied with a red ribbon, the prize bracelet"></div>
    <span class="prize-name">Veloriane</span>
  </aside>
</main>
</body>
</html>
```